Visitenkarten und Briefpapier für Beratungsunternehmen
Zielgruppe
Führungskräfte im Gesundheits- und Sozialwesen-
Aufgabenstellung
Wir suchen ein Set aus Briefpapier und Visitenkarten zu umserem Logo. Beides darf (muss nicht) beidseitig gestaltet werden.

```html
<!DOCTYPE html>
<html lang="de">
<head>
<meta charset="utf-8">
<title>KELMARANT Briefpapier</title>
<link href="https://fonts.googleapis.com/css2?family=Noto+Sans:wght@400&display=swap" rel="stylesheet">
<style>
  :root {
    --paper: #ffffff;
    --ink: #2b2b2b;
    --muted: #444444;
  }
  html, body { margin: 0; padding: 0; overflow: hidden; background: var(--paper); }
  .sheet {
    position: relative; width: 847px; height: 1200px; background: var(--paper);
    font-family: "Noto Sans", Verdana, sans-serif; color: var(--ink); overflow: hidden;
  }
  .brand {
    position: absolute; top: 32px; left: 640px; display: flex; align-items: center; gap: 8px;
  }
  .brand-mark { width: 14px; height: 14px; background: var(--ink); }
  .brand-name { font-size: 20px; font-weight: 400; color: var(--ink); letter-spacing: 0.5px; }
  .sender {
    position: absolute; top: 136px; left: 605px; font-size: 9.6px; line-height: 13.2px;
    color: var(--muted); letter-spacing: 0.3px;
  }
  .sender .row { display: flex; }
  .sender .label { width: 40px; }
  .recipient {
    position: absolute; top: 231px; left: 95px; font-size: 10.4px; line-height: 13.6px; letter-spacing: 0.6px;
  }
  .salutation-line {
    position: absolute; top: 399px; left: 95px; width: 515px; display: flex;
    justify-content: space-between; font-size: 10.4px; letter-spacing: 0.6px;
  }
  .body-copy {
    position: absolute; top: 424px; left: 95px; width: 515px; font-size: 10.4px;
    line-height: 13.6px; letter-spacing: 0.6px;
  }
  .body-copy p { margin: 0 0 13.6px; }
  .signature { margin-top: 18px; padding-left: 8px; }
  .legal {
    position: absolute; top: 1010px; left: 631px; font-size: 9.4px; line-height: 12.4px;
    color: var(--muted); letter-spacing: 0.3px;
  }
  .legal .row { display: flex; }
  .legal .label { width: 38px; }
</style>
</head>
<body>
<div class="sheet">
  <div class="brand">
    <span class="brand-mark"></span>
    <span class="brand-name">KELMARANT</span>
  </div>

  <div class="sender">
    <div>KELMARANT UG (hg)</div>
    <div>Lindenweg 14</div>
    <div>56733 Wernstadt</div>
    <div>Geschäftsführerin Marlene Odewig</div>
    <div>Telefon 0157.41 62 09</div>
    <div class="row"><span class="label">Fax</span><span>0157.41 62 10</span></div>
    <div class="row"><span class="label"></span><span>www.kelmarant.de</span></div>
    <div class="row"><span class="label">eMail</span><span>info@kelmarant.de</span></div>
  </div>

  <div class="recipient">
    <div>Month 00, 200x</div>
    <div>Addressee Name</div>
    <div>Company Name</div>
    <div>1234 Anywhere Avenue</div>
    <div>Suite #000</div>
    <div>City, State 00000-0000</div>
    <div>Country</div>
  </div>

  <div class="salutation-line">
    <span>Dear Addressee Name:</span>
    <span>Ort, der 01.02.03</span>
  </div>

  <div class="body-copy">
    <p>Andipsum dipsum nostis nulpute magnisis niatie te molor adignis sequips uscipisit, sit vel ipsuscing ent lut lan ulla feugait augueraesto odolore doluptatio conis dolor sismodo luptatuero do od dolore magnim dolor augvero eu facilis ea core estrud eugiat velis ad tat dio odolor augue magna corting eugait enim venibh et, quatmusan hendre tincinisi tisisl dolute moloreet atem velesequat alit aliquat, vel dolore facidiuis dolore dignis dolorper il eugiamconsed deliquamcon henis alis atum duis at.</p>
    <p>Bore del ute faccum vercill aorper sent alit, venis autet, quipsustio eugue vero dolore velendre euis nos nonse dolessim illa feum dolor sumsan ectet lortincin vulputat amet, qui esto conulput acil in eugait vel essequam zzriusto diam, velit wisisit autat.</p>
    <p>Obore dolor incip ea conummy nulput vel ullan henisim am in ute ercilliqui ex ent at, quis augiat, commod tis enis num delit lor acing elis dolorer se eugue feu facinci liquis aut lut nulluptat er sum zzrit vulla consequis accum incidunt iusci blaortio odoloreet pratum veliquatie modit, quat. Ut nummodo exercilisl irilliqu ipsusto dolesequat. Ut wisl in ute consequam ad diam vulputpat lan hent vel doloreet utat ver si.</p>
    <p>Vullaorem iusci blamcon seniamcommy nit lureetum dolore con ea faccum iureet prat. In utat acidunt nullum venismolum ing exer iusci bla augue magna consequi tem veliquis nostion utpat.</p>
    <p>Do ea acilisis dolore min ercing endre consequat. Ero consequis ad eugueriat, siscidunt laor sum iuscipis nullaoreet, velent ilit amconul laorperit lore diatum dui bla facipit irit alis ad dolorpe rostrud tem essequat praesequam, coreet ip er sim dit, velisim inciliquam, quis adigna feugue dolore et irilliaor.</p>
    <p>Adiam zzrit,</p>
    <div class="signature">Veliquatin Veraessi</div>
  </div>

  <div class="legal">
    <div>St.-Nr.: 12/345/0000/6</div>
    <div>Finanzamt Wernstadt</div>
    <div>HRB-Nr. A 1223456</div>
    <div>Kreisbank Wernstadt eG</div>
    <div class="row"><span class="label">Konto</span><span>123 456 78</span></div>
    <div class="row"><span class="label">BLZ</span><span>999 00 00</span></div>
    <div>IBAN</div>
    <div>DE56 999 0000 0099 0123 09</div>
    <div>SWIFT &nbsp;abccc 12345</div>
  </div>
</div>
</body>
</html>
```